Boat business cards

I'm looking for business cards with the two logos I've attached. I don't have an specific idea in mind and open to anything. All the usual info will be on the card. Name, position in company, nr, email, address, ect. The company rents out these two boats for charters and fishing.

```html
<!DOCTYPE html>
<html lang="en">
<head>
<meta charset="utf-8">
<title>Boat Charter Business Cards</title>
<link rel="stylesheet" href="https://fonts.googleapis.com/css2?family=Poppins:wght@400;600&display=swap">
<style>
  :root {
    --backdrop: #a9a9a9;
    --brown: #876643;
    --sky: #a9c7e6;
    --sky-deep: #7fa3cf;
    --paper: #ebebec;
    --cream: #f3ede4;
    --ink: #1d1f26;
    --steel: #5d6168;
  }
  * { box-sizing: border-box; margin: 0; padding: 0; }
  html, body { width: 1127px; height: 1200px; overflow: hidden; }
  body {
    background: var(--backdrop);
    font-family: "Poppins", sans-serif;
    position: relative;
  }
  .card {
    position: absolute;
    left: 323px;
    width: 514px;
    height: 295px;
  }
  .card-front { top: 264px; display: flex; }
  .card-back { top: 643px; background: var(--paper); }

  .details {
    width: 317px;
    height: 100%;
    background: var(--brown);
    color: var(--cream);
    position: relative;
  }
  .name {
    position: absolute; left: 25px; top: 44px;
    font-size: 21px; font-weight: 600; letter-spacing: 1.3px;
  }
  .role {
    position: absolute; left: 27px; top: 71px;
    font-size: 13px; font-weight: 400; letter-spacing: 0.4px;
  }
  .icons {
    position: absolute; left: 30px; top: 156px;
    display: flex; gap: 13px;
  }
  .icon {
    width: 24px; height: 24px; border-radius: 4px;
    background: var(--sky);
    display: flex; align-items: center; justify-content: center;
  }
  .divider {
    position: absolute; left: 29px; top: 196px;
    width: 228px; height: 1px; background: var(--cream);
  }
  .contact {
    position: absolute; left: 29px; top: 210px;
    list-style: none;
    font-size: 13px; line-height: 18px; letter-spacing: 0.3px;
  }

  .brand-panel {
    flex: 1;
    background: var(--sky);
    position: relative;
  }
  .yacht-art {
    position: absolute; left: 56px; top: 38px;
    width: 50px; height: 236px;
    background: linear-gradient(90deg, #ffffff 0%, #27262a 45%, #8a6440 100%);
    opacity: 0.85;
  }
  .yacht-name {
    position: absolute; left: 134px; top: 150px;
    transform: translate(-50%, -50%) rotate(90deg);
    white-space: nowrap;
    font-size: 26px; font-weight: 600; color: var(--ink);
    letter-spacing: 3px; line-height: 1;
  }

  .boat-art {
    position: absolute; left: 102px; top: 52px;
    width: 328px; height: 124px;
    background: linear-gradient(180deg, #dcdde0 0%, #c9cdd4 45%, var(--sky-deep) 80%, #9aa0a8 100%);
  }
  .boat-name {
    position: absolute; left: 108px; top: 184px;
    font-size: 38px; font-weight: 600; color: var(--steel);
    line-height: 1; letter-spacing: 1px;
  }
  .boat-place {
    position: absolute; left: 124px; top: 232px;
    font-size: 10px; font-weight: 600; color: var(--steel);
    line-height: 1.2;
  }
  .boat-model {
    position: absolute; left: 352px; top: 230px;
    font-size: 12px; font-weight: 600; color: var(--steel);
    line-height: 1.2;
  }
</style>
</head>
<body>
  <section class="card card-front">
    <div class="details">
      <h1 class="name">JOHNATHAN DOE</h1>
      <p class="role">ACCOUNT MANAGER</p>
      <div class="icons">
        <span class="icon">
          <svg width="14" height="14" viewBox="0 0 24 24"><path fill="#876643" d="M6.6 10.8a15.1 15.1 0 0 0 6.6 6.6l2.2-2.2c.3-.3.7-.4 1-.2 1.1.4 2.3.6 3.6.6.6 0 1 .4 1 1V20c0 .6-.4 1-1 1A17 17 0 0 1 3 4c0-.6.4-1 1-1h3.5c.6 0 1 .4 1 1 0 1.3.2 2.5.6 3.6.1.3 0 .7-.2 1z"/></svg>
        </span>
        <span class="icon">
          <svg width="15" height="12" viewBox="0 0 24 18"><rect x="1" y="1" width="22" height="16" rx="2" fill="#876643"/><path d="M2 3l10 7 10-7" fill="none" stroke="#a9c7e6" stroke-width="2"/></svg>
        </span>
        <span class="icon">
          <svg width="15" height="15" viewBox="0 0 24 24" fill="none" stroke="#876643" stroke-width="2"><circle cx="12" cy="12" r="10"/><ellipse cx="12" cy="12" rx="4" ry="10"/><path d="M2 12h20M4 7h16M4 17h16"/></svg>
        </span>
      </div>
      <div class="divider"></div>
      <ul class="contact">
        <li>123 456 7890</li>
        <li>EMAIL@DOMAIN.COM</li>
        <li>WWW.WEBSITE.COM</li>
      </ul>
    </div>
    <div class="brand-panel">
      <div class="yacht-art" role="img" aria-label="Side-view illustration of the Polar Tide motor yacht"></div>
      <p class="yacht-name">Polar Tide</p>
    </div>
  </section>

  <section class="card card-back">
    <div class="boat-art" role="img" aria-label="Side-view illustration of the Sea Breeze center-console fishing boat"></div>
    <p class="boat-name">Sea Breeze</p>
    <p class="boat-place">harbor point, bayside</p>
    <p class="boat-model">38SX</p>
  </section>
</body>
</html>
```